Flyer for a Unique Type of Tax Services

Please refer to the attached sample design for reference. Feel free to change the wording as needed. Here is the project brief:

Objective:
Objective of this flyer is to introduce our services which we are launching soon, which is new of a kind, to our potential customers i.e. online tax return preparation. By looking at the flyer we want our target audience to get convinced of our services and visit our website and register with us. They don’t have to pay anything to register.

Our Competitors:
Currently there are three main options available to get tax returns prepared. First is to buy tax software and get tax return prepared at own, this is the cheapest option. There are studies that suggest that people who are not well aware of tax laws there are chances they miss certain tax refunds by filing returns at their own and potentially lose money. Second option is to go to the local offices of nation-wide tax service companies like P&L Fenwick and Morrow Lindqvist. They open offices only during tax season i.e. Jan through April but they are not available other part of the year and their association with the customers is temporary. Third option is to go to a CPA office which are the most expensive and very few people go for this option.

Weaknesses of the Current Options:
By self-preparing tax returns, there are chances that one can overlook certain tax laws that can provide additional tax credits and exemptions to people and overall they could have got a higher tax refund from the Govt. but they may miss it.
By going to other competitors during the peak time when tax returns are due, there are high chances that they don't have enough time to do research to ensure maximum refunds based on the exact circumstances of the individuals at the peak time as many people come to them during that time. Also they are not available after the tax season to provide them any answers to their questions or provide them tax planning tips to help them save tax in the next season.
By going to the CPA office, they charge a lot of fees and also for any tax advice later during the year, they will charge additional fees.

What we are offering:
We are offering a new option i.e. online tax return preparation through experts. We'll charge the fees competitive to what people are paying to local tax providers. But we will be different than our competitors as we'll be providing value added service if they got their returns prepared through us. Value added services we will be free of any additional cost for our customers who'll get tax return prepared through us.

Our Target Audience:
Our target audience is any person or couple who go to the tax service providers like P&L Fenwick or Morrow Lindqvist to get their tax returns prepared.

How We are Different:
Here is the summary of the unique aspects of our business as compared to the competitors:
- Customers just pay us the price for preparing the annual return and price is comparable and competitive to what they have been paying to other providers.
- Unlike our competitors, we do extensive research to review the circumstances of our customers and explore applicable tax laws to make sure all available tax credits, exemptions, and deductions are taken for our customers, whereas our customers don't usually do such kind of research as during the peak tax season when customers approach them they usually don’t have time to do that kind of research. We start our association with our customers much sooner than the actual due date and this provides us time to do extensive research and we try our best that our customers could get higher tax returns.
- By just getting tax returns prepared through us, we enter into a long-term association with our customers and provide them complimentary tax planning tips throughout the year to help them save tax in the following year
- We are available to our customers year-round to provide complementary answers to any tax related questions without any additional cost e.g. how to save tax when buying a car, whether to buy or lease the care to save tax, for the sole-proprietor business how to save tax by using portion of the home as home-office, how to save tax by using personal car for personal business.
- We also provide answers to other basic financial advise related matters e.g. which insurance product is better, whether full insurance or term-life insurance to chose, how to save for the retirement etc.

Other Details:
Our logo has already been designed and we want the same logo to be used in the flyer. Our website address is: www.FiledRightAdvisor.com (it is still under construction but to get perspective of what we are trying to offer, visit this alternate website that it not final yet but will give an idea: http://www.filedrightadvisor.com/wordpress. Fyi, a video at this link is only a placeholder and not relevant to our services)

Industry/Entity Type

Construction

Requirements
Must have
• Please refer to the sample flyer attached. Feel free to change the design and language.
Should not have
• Please do not put any testimonial on the flyer as reflected in the under construction website.

```html
<!DOCTYPE html>
<html lang="en">
<head>
<meta charset="utf-8">
<title>FiledRight Advisor – Flyer</title>
<link href="https://fonts.googleapis.com/css2?family=Lato:wght@400;700;900&family=Open+Sans:wght@400;600&display=swap" rel="stylesheet">
<style>
  :root{
    --page:#e4e4e6;
    --paper:#ffffff;
    --navy:#27348b;
    --pill:#5b63b1;
    --red:#c8171e;
    --band-red:#cf1f26;
    --band-blue:#2c43a3;
    --ink:#2b2b2b;
    --grey-top:#d6d6d8;
    --grey-bottom:#f3f3f4;
    --photo-a:#f4f1ec;
    --photo-b:#d9cbb3;
  }
  *{box-sizing:border-box;margin:0;padding:0}
  html,body{width:1200px;height:968px;overflow:hidden;background:var(--page)}
  .flyer{position:absolute;left:320px;top:24px;width:560px;height:920px;background:var(--paper);box-shadow:0 4px 18px rgba(0,0,0,.18);overflow:hidden;font-family:"Lato",sans-serif}
  .hero-photo{position:absolute;left:150px;top:0;width:410px;height:452px;background:linear-gradient(160deg,var(--photo-a) 0%,var(--photo-b) 70%,#b9a789 100%)}
  .brand{position:absolute;left:40px;top:56px;display:flex;align-items:center;gap:10px}
  .brand-dot{width:30px;height:30px;border-radius:50%;background:var(--navy)}
  .brand-name{font-weight:900;font-size:34px;color:var(--navy);letter-spacing:-.5px;white-space:nowrap}
  .tagline{position:absolute;background:var(--pill);color:#fff;border-radius:8px;text-transform:uppercase;display:flex;align-items:center;padding:0 14px;white-space:nowrap;box-shadow:0 2px 4px rgba(0,0,0,.2)}
  .tagline-1{left:40px;top:212px;width:314px;height:44px;font-size:18px}
  .tagline-2{left:18px;top:262px;width:278px;height:50px;font-size:21px}
  .call{position:absolute;left:322px;top:392px;height:58px;display:flex}
  .call-icon{width:48px;background:var(--band-blue);display:flex;align-items:center;justify-content:center;border-radius:6px 0 0 6px}
  .call-text{width:168px;background:var(--band-red);color:#fff;font-size:15.5px;line-height:1.4;padding:7px 0 0 16px;border-radius:0 6px 6px 0;white-space:nowrap}
  .info{position:absolute;left:0;top:452px;width:560px;height:403px;background:linear-gradient(180deg,var(--grey-top),var(--grey-bottom))}
  .questions{position:absolute;left:38px;top:34px;width:256px;color:var(--navy);font-weight:700;font-size:17px;line-height:1.3}
  .questions p{margin-bottom:14px}
  .questions em{font-style:normal;color:var(--red)}
  .different{position:absolute;left:322px;top:26px;width:212px;color:var(--ink)}
  .different h2{font-weight:400;font-size:14px;letter-spacing:.2px;margin-bottom:10px}
  .different p{font-family:"Open Sans",sans-serif;font-size:6.6px;line-height:1.45;text-align:justify;margin-bottom:5px}
  .contact-web{position:absolute;left:388px;top:790px;width:172px;height:82px;background:var(--band-blue);color:#fff;font-size:9px;padding:14px 0 0 16px;white-space:nowrap}
  .contact-web div{display:flex;align-items:center;gap:10px;margin-bottom:10px}
  .address{position:absolute;left:0;top:855px;width:388px;height:65px;background:var(--band-red);color:#fff;display:flex;align-items:center;gap:16px;padding-left:62px;font-size:11px;line-height:1.35}
</style>
</head>
<body>
<main class="flyer">
  <div class="hero-photo" role="img" aria-label="Photo of a smiling tax consultant in glasses giving a thumbs-up beside a calculator and keyboard"></div>

  <div class="brand">
    <span class="brand-dot"></span>
    <span class="brand-name">FiledRight Advisor</span>
  </div>

  <div class="tagline tagline-1">Our business is to make your</div>
  <div class="tagline tagline-2">Taxes perfectly flow</div>

  <div class="call">
    <div class="call-icon">
      <svg width="22" height="22" viewBox="0 0 24 24"><path fill="#fff" d="M6.6 10.8a15 15 0 0 0 6.6 6.6l2.2-2.2c.3-.3.7-.4 1-.2 1.1.4 2.3.6 3.6.6.6 0 1 .4 1 1V20c0 .6-.4 1-1 1A17 17 0 0 1 3 4c0-.6.4-1 1-1h3.5c.6 0 1 .4 1 1 0 1.3.2 2.5.6 3.6.1.3 0 .7-.2 1z"/></svg>
    </div>
    <div class="call-text">CALL US NOW<br>(+1)-212-555-0148</div>
  </div>

  <section class="info">
    <div class="questions">
      <p>Does your Tax Return Prepare has time to do <em>Extensive Research</em> for you to help you get <em>maximum refunds</em>?</p>
      <p>Do you get year-round <em>Free Advice</em> regarding your <em>Tax related Questions</em> from your exiting Tax Service Provider?</p>
      <p>Does your existing Tax Service Provider give you <em>Complementary Tax Planning Tips</em> throughout the year to help you <em>save tax in the following year</em>?</p>
    </div>
    <div class="different">
      <h2>HOW WE ARE DIFFERENT</h2>
      <p>Customers just pay us the price for preparing the annual return and price is comparable and competitive to what they have been paying to other providers.</p>
      <p>Unlike our competitors, we do extensive research to review the circumstances of our customers and explore applicable tax laws to make sure all available tax credits, exemptions, and deductions are taken for our customers, whereas our customers don't usually do such kind of research as during the peak tax season when customers approach them they usually don't have time to do that kind of research. We start our association with our customers much sooner than the actual due date and this provides us time to do extensive research and we try our best that our customers could get higher tax returns.</p>
      <p>By just getting tax returns prepared through us, we enter into a long-term association with our customers and provide them complimentary tax planning tips throughout the year to help them save tax in the following year</p>
      <p>We are available to our customers year-round to provide complementary answers to any tax related questions without any additional cost e.g. how to save tax when buying a car, whether to buy or lease the care to save tax, for the sole-proprietor business how to save tax by using portion of the home as home-office, how to save tax by using personal car for personal business.</p>
      <p>We also provide answers to other basic financial advise related matters e.g. which insurance product is better, whether full insurance or term-life insurance to chose, how to save for the retirement etc.</p>
    </div>
  </section>

  <div class="contact-web">
    <div>
      <svg width="16" height="14" viewBox="0 0 16 14"><rect x="1" y="1" width="14" height="9" fill="none" stroke="#fff" stroke-width="1.4"/><path d="M5 13h6M8 10v3" stroke="#fff" stroke-width="1.4"/></svg>
      <span>www.filedrightadvisor.com</span>
    </div>
    <div>
      <svg width="16" height="12" viewBox="0 0 16 12"><rect x="1" y="1" width="14" height="10" fill="none" stroke="#fff" stroke-width="1.4"/><path d="M1 1l7 6 7-6" fill="none" stroke="#fff" stroke-width="1.4"/></svg>
      <span>hello@filedrightadvisor.com</span>
    </div>
  </div>

  <div class="address">
    <svg width="18" height="26" viewBox="0 0 18 26"><path fill="#fff" d="M9 0a9 9 0 0 0-9 9c0 7 9 17 9 17s9-10 9-17a9 9 0 0 0-9-9zm0 13a4 4 0 1 1 0-8 4 4 0 0 1 0 8z"/></svg>
    <span>Harbor Point Center, near<br>Elm Plaza, Newyork, NW</span>
  </div>
</main>
</body>
</html>
```